Letterhead Design for Law Firm that Specializes in Property Damage Litigation

We are looking for a redesign of our letterhead. Our current letterhead lists all of our current staff members and we'd like to come up with a design that does NOT list all of the staff members so that it does not need to be updated with every newly hired employee. Must be in editable format.

We are a law firm that specializes in property damage, so we need something that is professional, yet modern. The final design should use our existing logo and should use a blue color scheme (alternate colors would be gray, black, and white).

Industry/Entity Type

Legal

Colors
0054AA
0677BA
7BADD7
CADEEF
E8F1F8

```html
<!DOCTYPE html>
<html lang="en">
<head>
<meta charset="utf-8">
<title>Hartwell Ames &amp; Corbin — Letterhead</title>
<link href="https://fonts.googleapis.com/css2?family=Cinzel:wght@500&family=Montserrat:wght@400;500&display=swap" rel="stylesheet">
<style>
  :root {
    --paper: #ebedf1;
    --navy: #1d3461;
    --slate: #676a6b;
    --ink: #2c2f33;
    --muted: #6b6e72;
  }
  * { margin: 0; padding: 0; box-sizing: border-box; }
  html, body { width: 849px; height: 1200px; overflow: hidden; background: var(--paper); }
  .letterhead { position: relative; width: 849px; height: 1200px; background: var(--paper); }

  .side-band { position: absolute; left: 0; top: 0; width: 27px; height: 1200px; }
  .side-band__primary { height: 879px; background: var(--navy); }
  .side-band__secondary { height: 321px; background: var(--slate); }

  .brand { position: absolute; left: 85px; top: 72px; }
  .brand__row { display: flex; align-items: center; gap: 18px; }
  .brand__mark { width: 40px; height: 40px; background: var(--navy); flex: none; }
  .brand__name {
    font-family: "Cinzel", serif; font-weight: 500; color: var(--navy);
    font-size: 27px; line-height: 29px; letter-spacing: 1px;
  }
  .brand__tagline {
    margin-top: 12px; font-family: "Montserrat", sans-serif; font-weight: 500;
    font-size: 10.5px; letter-spacing: 2.6px; color: var(--muted); text-transform: uppercase;
  }

  .contact-bar {
    position: absolute; top: 1131px; left: 68px; right: 50px;
    font-family: "Montserrat", sans-serif; font-size: 10.5px; color: var(--ink); line-height: 13px;
  }
  .contact-item { position: absolute; top: 0; display: flex; align-items: flex-start; gap: 9px; }
  .contact-item svg { width: 14px; height: 14px; flex: none; stroke: var(--muted); fill: none; stroke-width: 1.2; }
  .contact-item--phone { left: 0; }
  .contact-item--email { left: 151px; }
  .contact-item--web { left: 343px; }
  .contact-item--address { left: 524px; }
</style>
</head>
<body>
<main class="letterhead">
  <div class="side-band">
    <div class="side-band__primary"></div>
    <div class="side-band__secondary"></div>
  </div>

  <header class="brand">
    <div class="brand__row">
      <span class="brand__mark"></span>
      <h1 class="brand__name">Hartwell<br>Ames &amp;<br>Corbin</h1>
    </div>
    <p class="brand__tagline">The Property Damage Attorneys</p>
  </header>

  <footer class="contact-bar">
    <div class="contact-item contact-item--phone">
      <svg viewBox="0 0 16 16"><path d="M3 1.5l2.5 0 1.2 3-1.6 1.2c.8 1.8 2.4 3.4 4.2 4.2l1.2-1.6 3 1.2v2.5c0 .8-.7 1.5-1.5 1.5C6.5 13.5 2.5 9.5 1.5 3c0-.8.7-1.5 1.5-1.5z"/></svg>
      <span>(555) 214-0300</span>
    </div>
    <div class="contact-item contact-item--email">
      <svg viewBox="0 0 16 16"><rect x="1" y="3" width="14" height="10"/><path d="M1 3l7 6 7-6"/></svg>
      <span>hello@hacfirm.com</span>
    </div>
    <div class="contact-item contact-item--web">
      <svg viewBox="0 0 16 16"><circle cx="8" cy="8" r="6.5"/><ellipse cx="8" cy="8" rx="3" ry="6.5"/><path d="M1.5 8h13M2.5 5h11M2.5 11h11"/></svg>
      <span>www.hacfirm.com</span>
    </div>
    <div class="contact-item contact-item--address">
      <svg viewBox="0 0 16 16"><path d="M8 15s-5-5.2-5-8.5a5 5 0 0 1 10 0C13 9.8 8 15 8 15z"/><circle cx="8" cy="6.5" r="1.8"/></svg>
      <span>480 Linden Avenue Suite 900,<br>Fairview, PA 19000</span>
    </div>
  </footer>
</main>
</body>
</html>
```